Bright Lantern Path (BRLP) Business Card - company with a mission

Note* The file attached... orange with "Bright Lantern PATH" (in CAPS) is our logo. I am also open to having the text "bright lantern path" OUTSIDE the orange round logo for business card (so yes, you may take the text out).

The info: (the following info are separate. So either you can use Martin or Beatrice for now, but that will be 2 separate cards, not together in one card. Thanks!!

Martin K Doyle
202.555.0147
martin@brightlanternpath.example
Managing Partner

Beatrice M Orr
202.555.0183
beatrice@brightlanternpath.example
Managing Partner

Our website: www.brightlanternpath.example

BRLP LLC stands for Bright Lantern Path (non profit arm is called lantern path foundation)—our business is based out of New York City and has a non-profit arm where for every bar of soap you purchase, we donate a bar (don’t want any designs that limits us to only soap). Currently working with South Africa. We want the focus to be organic/natural soap with a mission.

Looking for a clean, fresh design.

Industry/Entity Type

Non-Profit

Requirements
Must have
• Clean, fresh, refreshing. Design should not be too busy.

```html
<!DOCTYPE html>
<html lang="en">
<head>
<meta charset="utf-8">
<title>Bright Lantern Path – Business Card</title>
<link href="https://fonts.googleapis.com/css2?family=Open+Sans:wght@400;600;700&display=swap" rel="stylesheet">
<style>
  :root {
    --stage: #d6d6d6;
    --paper: #ffffff;
    --apricot: #e2a56f;
    --apricot-deep: #d9995f;
    --ink-light: #ffffff;
  }
  html, body {
    margin: 0;
    width: 1200px;
    height: 900px;
    overflow: hidden;
    background: var(--stage);
    font-family: "Open Sans", Arial, sans-serif;
  }
  .canvas {
    width: 1200px;
    height: 900px;
    display: flex;
    align-items: center;
    justify-content: center;
    gap: 60px;
  }
  .card {
    width: 520px;
    height: 298px;
    position: relative;
    box-sizing: border-box;
    box-shadow: 0 2px 6px rgba(0,0,0,0.12);
  }
  /* Front */
  .card--front {
    background: var(--paper);
    display: flex;
    align-items: center;
    justify-content: center;
  }
  .brand-badge {
    width: 176px;
    height: 176px;
    border-radius: 50%;
    background: var(--apricot);
    display: flex;
    flex-direction: column;
    align-items: center;
    justify-content: center;
    color: var(--ink-light);
    font-weight: 600;
    text-align: center;
  }
  .brand-badge__name {
    font-size: 44px;
    line-height: 1;
    letter-spacing: 1px;
  }
  .brand-badge__full {
    font-size: 13px;
    margin-top: 8px;
    letter-spacing: 0.5px;
  }
  /* Back */
  .card--back {
    background: linear-gradient(135deg, var(--apricot) 0%, var(--apricot-deep) 100%);
    color: var(--ink-light);
    padding: 30px 34px;
  }
  .contact__name {
    font-size: 17px;
    font-weight: 600;
    margin: 0;
  }
  .contact__role {
    font-size: 14px;
    margin: 2px 0 0;
  }
  .contact__details {
    position: absolute;
    left: 34px;
    bottom: 30px;
    margin: 0;
    padding: 0;
    list-style: none;
    font-size: 13px;
    line-height: 1.6;
  }
  .contact__label { font-weight: 700; }
  .contact__web { font-weight: 700; font-size: 14px; }
  .back-wordmark {
    position: absolute;
    right: 34px;
    top: 96px;
    font-size: 72px;
    font-weight: 600;
    line-height: 1;
    letter-spacing: 2px;
  }
</style>
</head>
<body>
<main class="canvas">
  <section class="card card--front" aria-label="Card front">
    <div class="brand-badge">
      <span class="brand-badge__name">BRLP</span>
      <span class="brand-badge__full">bright lantern path</span>
    </div>
  </section>

  <section class="card card--back" aria-label="Card back">
    <p class="contact__name">Beatrice M Orr</p>
    <p class="contact__role">managing partner</p>
    <div class="back-wordmark">BRLP</div>
    <ul class="contact__details">
      <li><span class="contact__label">t:</span> 202.555.0183</li>
      <li><span class="contact__label">e:</span> beatrice@brightlanternpath.example</li>
      <li class="contact__web">www.brightlanternpath.example</li>
    </ul>
  </section>
</main>
</body>
</html>
```